Urgent seeking Cover Design for event

An Outdoor Movie Event company in singapore is seeking for a Cover Design to be placed on Quorvent for an outdoor movie event at a location called Halvern Gardens.
Cover design size is 920px by 450px
We have provided images in this project for your side to come out with something suitable but not too complicated.
We urgently need the design which can be in PDF format for easy editing on our ends. We also need all readable and editable working files.

Target Market(s)

movie goers

Colors

Designer to choose colors to be used in the design.

Requirements
Must have
• Simple design to incorporate images provided if able to.
Nice to have
• Cover size to be 920px by 450px
Should not have
• Not be too messy

```html
<!DOCTYPE html>
<html lang="en">
<head>
<meta charset="utf-8">
<title>Outdoor Movie Event – Halvern Gardens</title>
<link rel="stylesheet" href="https://fonts.googleapis.com/css2?family=Oswald:wght@400;500&family=Open+Sans:wght@400;600&display=swap">
<style>
  :root {
    --night-deep: #1a1540;
    --night-indigo: #2a1f5c;
    --magenta-glow: #b3205f;
    --teal-glow: #1c6f74;
    --marquee-teal: #4fd3c7;
    --marquee-teal-dark: #23a89e;
    --bulb-white: #f4fffd;
    --panel-white: #ffffff;
    --ink-dark: #3a3a3a;
    --text-white: #ffffff;
    --logo-grey: #8c8c8c;
  }
  html, body {
    margin: 0;
    padding: 0;
    width: 1200px;
    height: 587px;
    overflow: hidden;
    background: var(--night-deep);
  }
  .cover {
    position: relative;
    width: 1200px;
    height: 587px;
    overflow: hidden;
  }
  .night-sky {
    position: absolute;
    inset: 0;
    background:
      radial-gradient(ellipse 560px 200px at 600px 90px, rgba(179,32,95,0.95), rgba(179,32,95,0) 100%),
      radial-gradient(ellipse 700px 220px at 560px 560px, rgba(28,111,116,0.9), rgba(28,111,116,0) 100%),
      linear-gradient(180deg, var(--night-indigo) 0%, var(--night-deep) 100%);
  }
  .snack-art {
    position: absolute;
    left: 86px;
    top: 78px;
    width: 196px;
    height: 182px;
    border-radius: 18px;
    background: linear-gradient(135deg, #e8313f 0%, #f3c7a0 100%);
  }
  .show-sign-art {
    position: absolute;
    left: 456px;
    top: 56px;
    width: 308px;
    height: 146px;
    border-radius: 6px;
    background: linear-gradient(180deg, #4fd3c7 0%, #2a8f8a 60%, #161616 100%);
  }
  .marquee {
    position: absolute;
    left: 350px;
    top: 202px;
    width: 532px;
    height: 304px;
  }
  .marquee-text {
    position: absolute;
    left: 378px;
    top: 232px;
    width: 476px;
    height: 244px;
    text-align: center;
    color: var(--ink-dark);
  }
  .event-title {
    margin: 20px 0 0;
    font-family: 'Oswald', sans-serif;
    font-weight: 400;
    font-size: 62px;
    line-height: 76px;
    letter-spacing: 6px;
  }
  .event-venue {
    margin: 22px 0 0;
    font-family: 'Open Sans', sans-serif;
    font-size: 21px;
    color: var(--ink-dark);
  }
  .event-date {
    position: absolute;
    left: 920px;
    top: 202px;
    width: 220px;
    margin: 0;
    text-align: center;
    font-family: 'Oswald', sans-serif;
    font-weight: 400;
    font-size: 42px;
    line-height: 68px;
    letter-spacing: 5px;
    color: var(--text-white);
  }
  .organizer {
    position: absolute;
    left: 930px;
    top: 428px;
    width: 200px;
    text-align: center;
    color: var(--text-white);
  }
  .organizer-label {
    margin: 0;
    font-family: 'Open Sans', sans-serif;
    font-size: 17px;
  }
  .organizer-name {
    display: inline-flex;
    align-items: center;
    gap: 8px;
    margin-top: 6px;
    font-family: 'Oswald', sans-serif;
    font-weight: 500;
    font-size: 26px;
    letter-spacing: 1px;
    color: var(--text-white);
  }
  .organizer-mark {
    width: 22px;
    height: 22px;
    background: var(--logo-grey);
  }
</style>
</head>
<body>
<main class="cover">
  <div class="night-sky" role="img" aria-label="Starry night sky with scattered stars over a magenta to teal glow"></div>

  <div class="snack-art" role="img" aria-label="Illustration of a red soda cup with straw and a striped popcorn box"></div>

  <div class="show-sign-art" role="img" aria-label="Illustrated rooftop sign reading SHOW in teal light bulb letters on a black truss stand"></div>

  <svg class="marquee" viewBox="0 0 532 304" aria-hidden="true">
    <rect x="2" y="2" width="528" height="300" rx="12" fill="var(--marquee-teal)" stroke="var(--marquee-teal-dark)" stroke-width="3"/>
    <rect x="26" y="28" width="480" height="248" rx="4" fill="var(--marquee-teal-dark)"/>
    <rect x="28" y="30" width="476" height="244" fill="var(--panel-white)"/>
    <g fill="var(--bulb-white)">
      <circle cx="24" cy="14" r="5"/><circle cx="64" cy="14" r="5"/><circle cx="104" cy="14" r="5"/>
      <circle cx="145" cy="14" r="5"/><circle cx="185" cy="14" r="5"/><circle cx="226" cy="14" r="5"/>
      <circle cx="266" cy="14" r="5"/><circle cx="306" cy="14" r="5"/><circle cx="347" cy="14" r="5"/>
      <circle cx="387" cy="14" r="5"/><circle cx="428" cy="14" r="5"/><circle cx="468" cy="14" r="5"/>
      <circle cx="508" cy="14" r="5"/>
      <circle cx="24" cy="290" r="5"/><circle cx="64" cy="290" r="5"/><circle cx="104" cy="290" r="5"/>
      <circle cx="145" cy="290" r="5"/><circle cx="185" cy="290" r="5"/><circle cx="226" cy="290" r="5"/>
      <circle cx="266" cy="290" r="5"/><circle cx="306" cy="290" r="5"/><circle cx="347" cy="290" r="5"/>
      <circle cx="387" cy="290" r="5"/><circle cx="428" cy="290" r="5"/><circle cx="468" cy="290" r="5"/>
      <circle cx="508" cy="290" r="5"/>
      <circle cx="14" cy="50" r="5"/><circle cx="14" cy="88" r="5"/><circle cx="14" cy="126" r="5"/>
      <circle cx="14" cy="164" r="5"/><circle cx="14" cy="202" r="5"/><circle cx="14" cy="240" r="5"/>
      <circle cx="518" cy="50" r="5"/><circle cx="518" cy="88" r="5"/><circle cx="518" cy="126" r="5"/>
      <circle cx="518" cy="164" r="5"/><circle cx="518" cy="202" r="5"/><circle cx="518" cy="240" r="5"/>
    </g>
  </svg>

  <div class="marquee-text">
    <h1 class="event-title">OUTDOOR<br>MOVIE EVENT</h1>
    <p class="event-venue">At Halvern Gardens</p>
  </div>

  <p class="event-date">28 TH<br>AUGUST<br>2019</p>

  <div class="organizer">
    <p class="organizer-label">Organized by</p>
    <div class="organizer-name"><span class="organizer-mark"></span>LUMENRAY</div>
  </div>
</main>
</body>
</html>
```